Community-based social network needs a new landing page

We need a landing page for a local social network in Singapore called "LaneSharely.sg". It is a website that help neighbours to connect with each other for mutual benefits such as providing professional/non-professional services, sharing items, and neighbourly help, etc.

There is an existing website but we want to completely revamp it. It is most important that the new landing page communicates that the neighbourhood has skills and services for people to discover.

The final design of the landing page should be modern, and communicates a sense of community and vibrancy. As a matter of priority, more real estate should be accorded to the neighbours providing services elements.

We have drafted 2 reference sites that communicates the key ideas/user propositions for your easy reference:
http://tavrelko82.exampleweb.com/lanesharely
http://tavrelko82.exampleweb.com/lanesharely2

As long as the key ideas/user propositions are kept to, we are open to any design proposals. I.e. you do not have to follow the design layout of the reference sites

Target Market(s)

Our target market is primarily the Singapore community, includes all genders, education levels and occupations, aged between 17-45 years old.

In the file uploaded, you will find pictures of Singapore neighbourhoods and people of local ethnicities. Please use them, but you may arrange and add further filters to better enhance them

Industry/Entity Type

Real Estate

Requirements
Nice to have
• Landing page could be similar to that of www.gatherova.com, not just at the top, but also the way the other categories are presented at the bottom.

```html
<!DOCTYPE html>
<html lang="en">
<head>
<meta charset="utf-8">
<title>LaneSharely.sg</title>
<link href="https://fonts.googleapis.com/css2?family=Ropa+Sans&family=Anton&family=Kaushan+Script&display=swap" rel="stylesheet">
<style>
:root{
  --navy:#1c3550;--teal:#4aa3b8;--yellow:#f2b81c;--green:#8dc03a;--red:#d8232a;
  --ink:#2a2a2a;--body:#4a4a4a;--muted:#777;--header:#f7f7f7;--panel:#f0f0f0;
  --box:#f6f6f6;--line:#dcdcdc;--footer:#e6e6e6;--base:#0d0d0d;
}
*{margin:0;padding:0;box-sizing:border-box}
html,body{width:1091px;height:1200px;overflow:hidden;background:#fff}
body{position:relative;font-family:"Ropa Sans",sans-serif;color:var(--ink)}
.abs{position:absolute}
.site-header{left:0;top:0;width:1091px;height:125px;background:var(--header);border-bottom:1px solid #e2e2e2}
.brand{left:146px;top:46px;display:flex;align-items:center;gap:6px;font-size:27px;color:#555;letter-spacing:.5px;white-space:nowrap}
.brand i{width:20px;height:20px;background:var(--red);display:block}
.nav a{position:absolute;top:48px;width:94px;height:23px;border-bottom:3px solid;font-size:15px;color:#333;text-decoration:none;padding-left:3px;line-height:15px;white-space:nowrap;overflow:visible}
.hero{left:147px;top:133px;width:796px;height:386px;overflow:hidden;
  background:linear-gradient(180deg,#5a6f86 0%,#8da0b4 22%,#e8e2d4 40%,#d9c9a6 60%,#9c8a5e 85%,#3e4b2e 100%)}
.hero h1{position:absolute;left:25px;top:190px;font-family:"Anton",sans-serif;font-weight:400;font-size:56px;line-height:66px;color:#fff;letter-spacing:2px;white-space:nowrap;
  text-shadow:-2px -2px 0 #111,2px -2px 0 #111,-2px 2px 0 #111,2px 2px 0 #111}
.hero .script{position:absolute;left:22px;top:262px;width:560px;font-family:"Kaushan Script",cursive;font-size:31px;line-height:37px;color:var(--yellow);
  text-shadow:1px 1px 0 #3b2a00,-1px -1px 0 #3b2a00}
.hero .bar{position:absolute;left:0;bottom:0;width:100%;height:45px;background:rgba(20,20,20,.6);color:#fff;font-size:19.5px;line-height:45px;padding-left:21px;white-space:nowrap}
.service h2{font-weight:400;font-size:19px;color:#222;margin-bottom:6px;white-space:nowrap}
.service .photo{width:248px;height:105px;border:1px solid #ddd}
.service p{font-size:11.6px;line-height:15px;color:var(--body);margin-top:8px;padding-left:2px;white-space:nowrap}
.panel{left:144px;top:750px;width:801px;height:261px;background:var(--panel)}
.panel h3{position:absolute;top:20px;font-weight:400;font-size:16.5px;color:#222}
.members{left:15px;top:39px;width:170px;height:212px;background:var(--box);border:1px solid var(--line)}
.thumbs{position:absolute;left:9px;top:10px;display:grid;grid-template-columns:repeat(4,36px);gap:2px}
.thumbs span{width:36px;height:36px;display:block}
.join{position:absolute;left:9px;top:169px;width:152px;height:33px;border:1px solid #c99a0c;border-radius:3px;background:linear-gradient(#f7cd3b,#e6ab14);text-align:center;line-height:32px;font-size:15px;color:#5a4300}
.listings{left:201px;top:39px;width:299px;height:212px;background:var(--box);border:1px solid var(--line)}
.item{position:absolute;left:8px;display:flex;align-items:center;gap:8px;font-size:10.6px;line-height:13px;color:#333;width:285px}
.item .icon{width:33px;height:33px;flex:none;background:#fff;border:1px solid #e4e4e4;display:flex;align-items:center;justify-content:center}
.quick{left:520px;top:46px;width:260px}
.quick h4{font-weight:400;font-size:12.5px;color:#222}
.quick p{font-size:11.5px;line-height:15px;color:var(--body);margin-top:7px}
.quick hr{border:0;border-top:1px solid #d5d5d5;margin-top:10px;width:260px}
.pill{display:inline-block;border:1px solid #c8c8c8;background:#fff;font-size:9px;padding:2px 4px;border-radius:2px;color:#333;vertical-align:middle}
.social i{display:inline-block;width:21px;height:21px;margin-right:4px}
.site-footer{left:0;top:1025px;width:1091px;height:104px;background:var(--footer)}
.fcol{position:absolute;top:14px}
.fcol h5{font-weight:400;font-size:17.5px;color:#333;margin-bottom:10px;white-space:nowrap}
.fcol a{display:block;font-size:10.5px;color:#777;text-decoration:none;line-height:17px}
.base{left:0;top:1129px;width:1091px;height:71px;background:var(--base);color:#8a8a8a}
.base .mark{position:absolute;left:147px;top:9px;font-size:16px;color:#777;display:flex;align-items:center;gap:4px}
.base .mark i{width:12px;height:12px;background:#666;display:block}
.base p{position:absolute;left:147px;top:33px;font-size:10.5px;line-height:14px}
.base small{position:absolute;right:150px;top:40px;font-family:Arial,sans-serif;font-size:8.5px}
</style>
</head>
<body>
<header class="abs site-header">
  <div class="abs brand"><i></i>LaneSharely.sg</div>
  <nav class="nav">
    <a style="left:433px;border-color:var(--navy)">Home</a>
    <a style="left:537px;border-color:var(--teal)">About us</a>
    <a style="left:642px;border-color:var(--yellow)">Login</a>
    <a style="left:746px;border-color:var(--green)">Friendbook Login</a>
    <a style="left:850px;border-color:var(--red)">Register</a>
  </nav>
</header>

<section class="abs hero" role="img" aria-label="Singapore public housing blocks under a cloudy sky">
  <h1>WHAT DO YOU NEED?</h1>
  <div class="script">Crowd source from the 50,000 people<br>living around you</div>
  <div class="bar">or CONTRIBUTE to your neighbourhood's services and items pool. Take a FREE listing today!</div>
</section>

<section class="abs service" style="left:146px;top:543px">
  <h2>PROFESSIONAL SERVICES</h2>
  <div class="photo" role="img" aria-label="Office team reviewing documents at a meeting table" style="background:linear-gradient(135deg,#cfd9e4,#8fa2b6 50%,#e4e6e8)"></div>
  <p>Offer or hire a professional service nearby. Charge<br>a "lower" neighbourhood rate since you save on<br>transport costs!</p>
</section>
<section class="abs service" style="left:417px;top:543px">
  <h2>NON-PROFESSIONAL SERVICES</h2>
  <div class="photo" role="img" aria-label="Hand signing a paper form" style="background:linear-gradient(180deg,#3a3a40,#9a9aa0 45%,#f2f2f2 70%)"></div>
  <p>You could be a student, an enthusiast, a hobbyist,<br>or just someone with time and muscle, but you<br>could be good enough for your neighbours to hire.</p>
</section>
<section class="abs service" style="left:692px;top:543px">
  <h2>SHARE &amp; HELP</h2>
  <div class="photo" role="img" aria-label="Fingers holding a keyboard key marked share and help" style="background:linear-gradient(90deg,#fafafa,#e8b59a 40%,#d89a7c 70%,#f6f6f6)"></div>
  <p>There are many ways to contribute to your neigh-<br>bourhood's pool of resources!</p>
</section>

<section class="abs panel">
  <h3 style="left:18px">Latest members</h3>
  <h3 style="left:203px">Latest listings</h3>
  <h3 style="left:520px">Quick links</h3>
  <div class="abs members">
    <div class="thumbs" role="img" aria-label="Profile photos of newest members">
      <span style="background:#6d7a6a"></span><span style="background:#4e5b48"></span><span style="background:#bdbdbd"></span><span style="background:#2c2a4a"></span>
      <span style="background:#8a7b62"></span><span style="background:#9b8a70"></span><span style="background:#a7b2bd"></span><span style="background:#b86b4a"></span>
      <span style="background:#6b5040"></span><span style="background:#4a6b3a"></span><span style="background:#8fa0c8"></span><span style="background:#8a7060"></span>
      <span style="background:#b04a4a"></span><span style="background:#3a3a3a"></span><span style="background:#d0d0d0"></span><span style="background:#5a4a40"></span>
    </div>
    <div class="join">JOIN NOW</div>
  </div>
  <div class="abs listings">
    <div class="item" style="top:7px"><span class="icon"><svg width="18" height="18"><rect x="3" y="5" width="5" height="9" fill="#999"/><rect x="10" y="3" width="5" height="9" fill="#999"/></svg></span>KelvinT is selling Mrcro / Nano Sim<br>Adapters</div>
    <div class="item" style="top:49px"><span class="icon"><svg width="18" height="18"><path d="M3 15 L9 5 L10 11 L15 3" stroke="#999" stroke-width="2" fill="none"/></svg></span>JMK wants to offer Electrical Repair (DIY)</div>
    <div class="item" style="top:87px"><span class="icon"><svg width="18" height="18"><rect x="5" y="7" width="8" height="8" fill="#999"/><path d="M13 9 L17 5" stroke="#999" stroke-width="2"/></svg></span>Benny lim wants to offer I can help water your plants while you're overseas! I'm dependable and detailed</div>
    <div class="item" style="top:130px"><span class="icon"><svg width="18" height="18"><path d="M5 2 L4 16 M13 2 L14 16 M4 6 H13 M4 10 H14 M4 14 H14" stroke="#999" stroke-width="1.6"/></svg></span>FaizalR has shared Ladder</div>
    <div class="item" style="top:167px"><span class="icon"><svg width="18" height="18"><rect x="2" y="4" width="12" height="5" fill="#999"/><rect x="5" y="9" width="4" height="7" fill="#999"/></svg></span>FaizalR has shared Electric Drill</div>
  </div>
  <div class="abs quick">
    <h4>Professional services pool:</h4>
    <p>Use the services of professionals living nearby at low rates, with no transport costs! And look out for the "verified" mark!</p>
    <hr>
    <div style="margin-top:20px;font-size:9px;color:#333"><span class="pill">Like</span>&nbsp; <span style="display:inline-block;width:9px;height:9px;background:#3b5998;vertical-align:middle"></span> Be the first of your friends to like this.</div>
    <div style="margin-top:8px"><span class="pill">Share</span> <span class="pill">0</span> &nbsp;&nbsp; <span class="pill">Follow @lanesharely</span> <span class="pill">170K followers</span></div>
    <div class="social" style="margin-top:10px"><i style="background:#3aa3d8"></i><i style="background:#3b5998"></i><i style="background:#c4302b"></i></div>
  </div>
</section>

<footer class="abs site-footer">
  <div class="fcol" style="left:146px"><h5>Want to know more?</h5><a>About Us</a><a>FAQ</a></div>
  <div class="fcol" style="left:355px"><h5>Using LaneSharely</h5><a>Terms of Use</a><a>Privacy Policy</a></div>
  <div class="fcol" style="left:565px"><h5>Get in touch</h5><a>Contact Us</a><a>Friendbook</a></div>
  <div class="fcol" style="left:722px;width:200px"><h5>Media mentions</h5>
    <a style="color:#666">“ New prints of our Flexiweave Reversible Tandees Wrist Wallets are now available. ”</a>
    <a style="color:#222;margin-top:2px">November 12, 2012, Tampines, SG</a></div>
</footer>
<div class="abs base">
  <div class="mark"><i></i>LaneSharely.sg</div>
  <p>LaneSharely.sg is a website of Lanecraft Pte. Ltd. We help you pool together physical items, efforts<br>and purchasing power with your favourite neighbours so that your can save money.</p>
  <small>© Copyright websitename . All Rights Reserved</small>
</div>
</body>
</html>
```